Corrowin Sack operates across the US and Australasia providing calico bags to small business through to large enterprise across all verticals. Our bags are the most premium in the market place and our customer service is second to none. Our competitive advantage lays in our competitive pricing, superior quality and outstanding customer service.

Industry/Entity Type

Business

Contact Information for Business Card

Corrowin Sack
Marisol Quenby
Managing Director
marisol@corrowinsack.com
www.corrowinsack.com.au
Mobile:- 0471 896 305
Level 3, 284 Harwick Street
Melbourne Victoria Australia 3000

```html
<!DOCTYPE html>
<html lang="en">
<head>
<meta charset="utf-8">
<title>Corrowin Sack — Business Card</title>
<link rel="stylesheet" href="https://fonts.googleapis.com/css2?family=Open+Sans:wght@400;600&display=swap">
<style>
  :root {
    --backdrop: #ecece8;
    --green-deep: #5c9e2b;
    --green-bright: #8cc63f;
    --green-text: #6aa632;
    --map-light: #a6d86a;
    --map-mid: #7dbb3c;
    --ink: #2b2b2b;
    --paper: #ffffff;
  }
  * { box-sizing: border-box; margin: 0; padding: 0; }
  html, body {
    width: 1200px; height: 900px; overflow: hidden;
    background: var(--backdrop);
    font-family: "Open Sans", sans-serif;
  }
  .canvas { position: relative; width: 1200px; height: 900px; }

  .card {
    position: absolute;
    width: 525px; height: 300px;
    border-radius: 3px;
    box-shadow: 0 6px 18px rgba(0,0,0,0.18);
    overflow: hidden;
  }

  /* Front */
  .card-front {
    left: 60px; top: 110px;
    background: linear-gradient(135deg, var(--green-deep) 0%, #72b234 55%, var(--green-bright) 100%);
  }
  .card-front .map-area {
    position: absolute; left: 150px; top: 40px;
    width: 225px; height: 210px;
    border-radius: 46% 40% 44% 38%;
    background: radial-gradient(circle at 55% 40%, #9bd45a 0%, #79b83a 70%, #6aaa30 100%);
    box-shadow: inset 0 2px 3px rgba(255,255,255,0.35), inset 0 -2px 4px rgba(0,0,0,0.15);
  }
  .card-front .brand-name {
    position: absolute; left: 0; right: 0; top: 135px;
    text-align: center;
    font-size: 26px; font-weight: 600;
    color: #e4f4cf; letter-spacing: 1px;
  }

  /* Back */
  .card-back {
    left: 615px; top: 480px;
    background: var(--paper);
  }
  .contact {
    position: absolute; left: 300px; top: 36px;
    color: var(--ink);
  }
  .contact .person-name {
    font-size: 17px; font-weight: 600; color: var(--green-text); line-height: 1.1;
  }
  .contact .role { font-size: 12px; margin-bottom: 14px; }
  .contact .address { font-size: 12px; line-height: 1.45; margin-bottom: 12px; }
  .contact .line {
    display: flex; align-items: center; gap: 8px;
    font-size: 12px; line-height: 1.7;
  }
  .contact .line svg { width: 11px; height: 11px; fill: var(--green-text); flex: none; }

  .card-back .map-area {
    position: absolute; left: 70px; top: 150px;
    width: 170px; height: 130px;
    border-radius: 46% 40% 44% 38%;
    background: radial-gradient(circle at 55% 40%, var(--map-light) 0%, var(--map-mid) 75%);
  }
  .card-back .brand-name {
    position: absolute; left: 60px; top: 200px; width: 190px;
    text-align: center;
    font-size: 18px; font-weight: 600; color: var(--ink);
  }
</style>
</head>
<body>
<main class="canvas">
  <section class="card card-front" aria-label="Card front">
    <div class="map-area" role="img" aria-label="Embossed map of Australia"></div>
    <div class="brand-name">Corrowin Sack</div>
  </section>

  <section class="card card-back" aria-label="Card back">
    <div class="contact">
      <p class="person-name">Marisol Quenby</p>
      <p class="role">Managing Director</p>
      <p class="address">Level 3, 284 Harwick Street<br>Melbourne Victoria Australia 3000</p>
      <p class="line">
        <svg viewBox="0 0 24 24" aria-hidden="true"><path d="M6.6 10.8a15.2 15.2 0 0 0 6.6 6.6l2.2-2.2a1 1 0 0 1 1-.25 11.4 11.4 0 0 0 3.6.57 1 1 0 0 1 1 1V20a1 1 0 0 1-1 1A17 17 0 0 1 3 4a1 1 0 0 1 1-1h3.5a1 1 0 0 1 1 1c0 1.25.2 2.45.57 3.57a1 1 0 0 1-.25 1z"/></svg>
        0471 896 305
      </p>
      <p class="line">
        <svg viewBox="0 0 24 24" aria-hidden="true"><path d="M2 5h20v14H2z M2 5l10 8 10-8" fill="currentColor"/><path d="M3 6l9 7 9-7v12H3z"/></svg>
        marisol@corrowinsack.com
      </p>
      <p class="line">
        <svg viewBox="0 0 24 24" aria-hidden="true"><path d="M10.6 13.4a1 1 0 0 1 0-1.4l3.5-3.5a1 1 0 1 1 1.4 1.4L12 13.4a1 1 0 0 1-1.4 0zM8.5 20a4.5 4.5 0 0 1-3.2-7.7l2.5-2.5 1.4 1.4-2.5 2.5a2.5 2.5 0 0 0 3.5 3.5l2.5-2.5 1.4 1.4-2.5 2.5A4.5 4.5 0 0 1 8.5 20zm7.7-5.8-1.4-1.4 2.5-2.5a2.5 2.5 0 0 0-3.5-3.5l-2.5 2.5-1.4-1.4 2.5-2.5a4.5 4.5 0 0 1 6.4 6.4z"/></svg>
        www.corrowinsack.com.au
      </p>
    </div>
    <div class="map-area" role="img" aria-label="Green map of Australia"></div>
    <div class="brand-name">Corrowin Sack</div>
  </section>
</main>
</body>
</html>
```